Design For Life Insurance Landing Page

Make Sure You Look At Attachments.

What we want from our design:
Light and clear design
Clear calls to action.
Clean, uncluttered design.
Space for 1500 words of content under various headings.
Incorporation of our brand colours (and suggestions for new colours that complement them)
Incorporation of logo into menu matched to page.

Some background:

We are rebranding our existing site around our new logo and coulours and want to move away from using blue heavily.

Our current site can be found here https://kestrova.co.uk/broadband/best-broadband-deals/

We will be using this competition to find someone to work with in future, our site will have around 50 landing pages in total.

https://www.pellorin.co.uk/life-insurance.htm

What we like about this page:
The header gives a clear call to action and shows the product variants clearly.
We also like the simple and clear menu.
Very clean design.

https://www.quibblestack.com/life-insurance/

Ample space for content.
Nice explainer graphics.
Clear concise design.

https://www.wendaroo.com/life-insurance

Clear calls to action
Nice use of brand colours, especially at the bottom.

Target Market(s)

Consumers in the UK

Requirements
Must have
• Use of our brand colours with suggestions to add to pallete.
• Clear calls to action.
• Clean, uncluttered design.
• Space for 1500 words of content under various headings.
• Incorporation of our brand colours (and suggestions for new colours that complement them)
• Incorporation of logo into menu matched to page.
• Must look as polished as the examples given.
Should not have
• Cluttered, messy design

```html
<!DOCTYPE html>
<html lang="en">
<head>
<meta charset="utf-8">
<title>Kestrova – Compare life insurance quotes</title>
<link rel="stylesheet" href="https://fonts.googleapis.com/css2?family=Open+Sans:wght@400;600;700&display=swap">
<style>
:root{
  --green:#8cc152;
  --green-dark:#6fa83a;
  --orange:#f39200;
  --ink:#222;
  --muted:#777;
  --line:#e3e3e3;
  --grey-band:#f4f4f4;
  --white:#fff;
}
*{box-sizing:border-box;margin:0;padding:0}
html,body{width:1200px;height:4675px;overflow:hidden}
body{font-family:"Open Sans",Arial,sans-serif;color:var(--ink);background:var(--white);position:relative}
section,header,footer{position:absolute;left:0;width:1200px}
.abs{position:absolute}

/* header */
.site-header{top:0;height:62px;background:var(--white)}
.brand{left:210px;top:14px;font-size:26px;font-weight:700;color:var(--ink);display:flex;align-items:center;gap:8px}
.brand-dot{width:12px;height:12px;background:var(--green);border-radius:50%}
.main-nav{right:200px;top:22px;display:flex;gap:26px;font-size:13px;font-weight:600}
.main-nav a{color:var(--ink);text-decoration:none}

/* hero */
.hero{top:62px;height:598px}
.hero-photo{inset:0;background:linear-gradient(100deg,#5e5a55 0%,#8d8377 35%,#c9bdb0 60%,#6b7f9c 85%,#d9d1c6 100%)}
.hero-title{left:210px;top:128px;width:420px;font-size:34px;line-height:42px;font-weight:700;color:var(--white)}
.hero-sub{left:210px;top:258px;font-size:12px;color:var(--white)}
.postcode{left:205px;top:325px;width:205px;height:44px;background:var(--white);border:none;font:12px "Open Sans",sans-serif;color:var(--muted);padding-left:16px;display:flex;align-items:center}
.btn{display:flex;align-items:center;justify-content:center;background:var(--orange);color:var(--white);font-size:13px;font-weight:600;text-decoration:none}
.hero .btn{left:415px;top:325px;width:165px;height:44px}

/* partners */
.partners{top:660px;height:105px;display:flex;justify-content:center;align-items:center;gap:46px;border-bottom:1px solid var(--line)}
.partner{width:60px;height:20px;background:#cfd4da;border-radius:3px}
.partner.round{width:32px;height:32px;border-radius:50%}

/* headings */
.section-title{font-size:24px;font-weight:600;color:var(--ink);text-align:center;width:1200px;left:0}
.copy{font-size:12px;line-height:20px;color:var(--muted)}

/* how it works */
.how{top:765px;height:435px}
.how .section-title{top:50px}
.step{width:240px;text-align:center}
.step-icon{width:110px;height:110px;border-radius:50%;background:#eef6e5;margin:0 auto 18px;display:flex;align-items:center;justify-content:center}
.step h3{font-size:13px;font-weight:700;margin-bottom:6px}

/* split bands */
.band-grey{background:var(--grey-band)}
.split-title{font-size:24px;line-height:31px;font-weight:600}
.compare{top:1200px;height:358px}
.compare-photo{left:577px;top:40px;width:530px;height:318px;background:radial-gradient(circle at 70% 40%,#f7a9c6,#f4d5e1 55%,#e9e9e9 80%)}
.why-take{top:1558px;height:359px}
.why-photo{left:280px;top:30px;width:235px;height:300px;background:linear-gradient(180deg,#f2f2f2,#d9cfc9 40%,#2c4d8f 80%)}
.benefits{top:1917px;height:358px}
.benefit-photo{left:560px;top:35px;width:560px;height:290px;background:linear-gradient(160deg,#f4f4f4,#e2e2e2 40%,#4a4a4a 55%,#e0c8b8 80%)}
.ticks{list-style:none}
.ticks li{display:flex;align-items:center;gap:12px;font-size:12px;color:var(--muted);margin-bottom:14px}

/* guides */
.guides{top:2275px;height:795px}
.guides .section-title{top:50px}
.card{width:240px;height:275px;border:1px solid var(--line);background:var(--white)}
.card-photo{height:193px}
.card p{font-size:12px;line-height:19px;padding:14px 18px;color:var(--ink)}

/* why choose */
.why-choose{top:3070px;height:490px;background:var(--green)}
.why-choose .section-title{top:50px;color:var(--white)}
.reason{width:380px;color:var(--white)}
.reason h4{font-size:13px;font-weight:700;display:flex;align-items:center;gap:10px;margin-bottom:8px}
.reason p{font-size:11px;line-height:19px;padding-left:42px}

/* faq */
.faq{top:3560px;height:617px}
.faq .section-title{top:70px}
.faq-list{left:224px;top:160px;width:720px;list-style:none}
.faq-list li{display:flex;align-items:flex-start;gap:14px;font-size:13px;font-weight:600;padding:13px 0;border-bottom:1px solid var(--line);min-height:53px}
.faq-list li span{line-height:20px}
.plus{flex:0 0 22px;height:22px;border:1px solid var(--green);border-radius:50%}

/* cta */
.cta{top:4177px;height:249px}
.cta-photo{inset:0;background:linear-gradient(90deg,#b9b1a7,#7d7f85 40%,#6e7a86 60%,#c9c3bb)}
.cta h2{top:70px;width:1200px;text-align:center;font-size:26px;font-weight:700;color:var(--white)}
.cta-sub{top:112px;width:1200px;text-align:center;font-size:12px;color:var(--white)}
.cta .btn{left:513px;top:150px;width:174px;height:44px}

/* footer */
.site-footer{top:4426px;height:249px}
.site-footer .brand{left:210px;top:32px}
.footer-about{left:210px;top:80px;width:320px;font-size:11px;line-height:17px;color:var(--muted)}
.footer-col h5{font-size:12px;font-weight:700;margin-bottom:8px}
.footer-col li{list-style:none;font-size:11px;line-height:18px;color:var(--muted)}
.social{display:flex;gap:8px;margin-top:8px}
.social i{width:22px;height:22px;border-radius:50%;border:1px solid #9fb7d6;display:block}
.legal{left:0;top:205px;width:1200px;text-align:center;font-size:10px;line-height:16px;color:var(--muted)}
</style>
</head>
<body>

<header class="site-header">
  <div class="brand abs">Kestrova<span class="brand-dot"></span></div>
  <nav class="main-nav abs">
    <a href="#">Home</a><a href="#">Compare</a><a href="#">Guides</a><a href="#">About Us</a><a href="#">Blog</a><a href="#">Contact Us</a>
  </nav>
</header>

<section class="hero">
  <div class="hero-photo abs" role="img" aria-label="Smiling couple embracing in a bright kitchen, holding a mug"></div>
  <h1 class="hero-title abs">Compare life insurance quotes and help protect what's important to you</h1>
  <p class="hero-sub abs">Save time and money by comparing leading life insurers all in one place</p>
  <div class="postcode abs">Enter Your Postcode</div>
  <a class="btn abs" href="#">Get Started Now</a>
</section>

<section class="partners" aria-label="Insurance partners">
  <span class="partner round"></span><span class="partner"></span><span class="partner"></span><span class="partner"></span><span class="partner round"></span><span class="partner"></span><span class="partner"></span><span class="partner"></span>
</section>

<section class="how">
  <h2 class="section-title abs">How It Works</h2>
  <div class="step abs" style="left:217px;top:123px">
    <div class="step-icon"><svg width="44" height="44" viewBox="0 0 44 44" fill="none" stroke="#8cc152" stroke-width="2"><rect x="9" y="6" width="22" height="30" rx="2"/><path d="M14 14h12M14 20h12M14 26h7"/><path d="M28 30l8-8 3 3-8 8h-3z"/></svg></div>
    <h3>Get acquainted</h3>
    <p class="copy">Provide us with a few details about you and the type of life insurance cover you're after.</p>
  </div>
  <div class="step abs" style="left:482px;top:123px">
    <div class="step-icon"><svg width="44" height="44" viewBox="0 0 44 44" fill="none" stroke="#8cc152" stroke-width="2"><rect x="8" y="8" width="28" height="28" rx="3"/><path d="M17 14v16M27 14v16M14 24h6M24 18h6"/></svg></div>
    <h3>Get fitted</h3>
    <p class="copy">Our qualified advisers will go through your options and help you get to the heart of your life insurance needs.</p>
  </div>
  <div class="step abs" style="left:746px;top:123px">
    <div class="step-icon"><svg width="44" height="44" viewBox="0 0 44 44" fill="none" stroke="#8cc152" stroke-width="2"><circle cx="18" cy="12" r="6"/><path d="M7 38c0-9 5-15 11-15s8 3 9 5"/><path d="M30 24l8 3v6c0 4-4 6-8 8-4-2-8-4-8-8v-6z"/><path d="M26 32l3 3 5-6"/></svg></div>
    <h3>Get covered</h3>
    <p class="copy">Knowing you're making an informed choice, you can select and buy a life insurance policy through the best.</p>
  </div>
</section>

<section class="compare band-grey">
  <h2 class="split-title abs" style="left:210px;top:62px;width:340px">Compare life insurance policies and save</h2>
  <p class="copy abs" style="left:210px;top:140px;width:345px">Life insurance gives the people you love a financial safety net when it matters most. Comparing a range of trusted providers side by side makes it easy to find cover that suits your budget, your family and your plans. Quick to do and free.</p>
  <div class="compare-photo abs" role="img" aria-label="Pink piggy bank wearing glasses beside a calculator"></div>
</section>

<section class="why-take">
  <div class="why-photo abs" role="img" aria-label="Smiling woman in a blue jumper clasping her hands"></div>
  <h2 class="split-title abs" style="left:608px;top:72px;width:340px">Why should I take out life insurance?</h2>
  <p class="copy abs" style="left:608px;top:150px;width:345px">If anyone relies on your income, a life policy could help them keep the home, pay the bills and plan ahead if you were no longer there. Premiums can cost less than you think, and the right cover can be tailored to match your mortgage and your family's needs.</p>
</section>

<section class="benefits band-grey">
  <h2 class="split-title abs" style="left:210px;top:50px;width:340px">Benefits of having life insurance</h2>
  <ul class="ticks abs" style="left:210px;top:130px;width:340px">
    <li><svg width="14" height="14" viewBox="0 0 14 14"><path d="M7 1l5 2v4c0 3-2 5-5 6-3-1-5-3-5-6V3z" fill="#8cc152"/><path d="M4.5 7l2 2 3-3.5" stroke="#fff" stroke-width="1.4" fill="none"/></svg>Protects your family's financial future</li>
    <li><svg width="14" height="14" viewBox="0 0 14 14"><path d="M7 1l5 2v4c0 3-2 5-5 6-3-1-5-3-5-6V3z" fill="#8cc152"/><path d="M4.5 7l2 2 3-3.5" stroke="#fff" stroke-width="1.4" fill="none"/></svg>Can be personalised to meet your needs</li>
    <li><svg width="14" height="14" viewBox="0 0 14 14"><path d="M7 1l5 2v4c0 3-2 5-5 6-3-1-5-3-5-6V3z" fill="#8cc152"/><path d="M4.5 7l2 2 3-3.5" stroke="#fff" stroke-width="1.4" fill="none"/></svg>Is a form of financial insurance against accidents</li>
    <li><svg width="14" height="14" viewBox="0 0 14 14"><path d="M7 1l5 2v4c0 3-2 5-5 6-3-1-5-3-5-6V3z" fill="#8cc152"/><path d="M4.5 7l2 2 3-3.5" stroke="#fff" stroke-width="1.4" fill="none"/></svg>Provides lump sum payments in the event of death, illness, or injury</li>
  </ul>
  <div class="benefit-photo abs" role="img" aria-label="Hands typing on a laptop beside a coffee cup, pen and small plant"></div>
</section>

<section class="guides">
  <h2 class="section-title abs">Find out more with our useful guides</h2>
  <article class="card abs" style="left:212px;top:131px"><div class="card-photo" role="img" aria-label="Older couple riding bicycles together" style="background:linear-gradient(160deg,#c7d9a8,#6e8f52)"></div><p>Which type of life insurance is right for you?</p></article>
  <article class="card abs" style="left:482px;top:131px"><div class="card-photo" role="img" aria-label="Laughing couple in sunglasses outdoors" style="background:linear-gradient(160deg,#d9b08a,#8c5a3c)"></div><p>What is life insurance, and is it important?</p></article>
  <article class="card abs" style="left:751px;top:131px"><div class="card-photo" role="img" aria-label="Person with arms raised on a hillside by the coast" style="background:linear-gradient(180deg,#e7d2b4,#b49370 60%,#6f5a45)"></div><p>Life insurance for high risk individuals</p></article>
  <article class="card abs" style="left:212px;top:443px"><div class="card-photo" role="img" aria-label="Cheerful woman in a red jacket" style="background:linear-gradient(160deg,#b9ccd9,#5d7a92 60%,#a64538)"></div><p>How to buy cheap life insurance</p></article>
  <article class="card abs" style="left:482px;top:443px"><div class="card-photo" role="img" aria-label="Woman sitting on a white car roof with a laptop" style="background:linear-gradient(180deg,#cfe0ec,#e9d08b 55%,#d9d9d9)"></div><p>How will my health affect my life insurance?</p></article>
  <article class="card abs" style="left:751px;top:443px"><div class="card-photo" role="img" aria-label="Woman with curly hair drinking from a mug" style="background:linear-gradient(160deg,#8a5b3d,#c98a58 50%,#3c6d8c)"></div><p>Which type of life insurance is right for you?</p></article>
</section>

<section class="why-choose">
  <h2 class="section-title abs">Why to Choose Us</h2>
  <div class="reason abs" style="left:203px;top:125px">
    <h4><svg width="30" height="22" viewBox="0 0 30 22" fill="none" stroke="#fff" stroke-width="1.6"><path d="M15 2l2.5 5 5.5.8-4 3.9.9 5.5L15 14.6 10.1 17.2l.9-5.5-4-3.9 5.5-.8z"/></svg>Transparent and professional service</h4>
    <p>We explain every policy in plain English, with no hidden fees and no pressure, so you can compare cover with confidence and choose the plan that truly fits your life and budget.</p>
  </div>
  <div class="reason abs" style="left:623px;top:125px">
    <h4><svg width="30" height="22" viewBox="0 0 30 22" fill="none" stroke="#fff" stroke-width="1.6"><rect x="3" y="5" width="24" height="14" rx="2"/><circle cx="15" cy="12" r="3.5"/></svg>We have the best prices on plans</h4>
    <p>Our panel of trusted UK insurers competes for your business, which means you see some of the most competitive premiums available and can switch or save in just a few minutes.</p>
  </div>
  <div class="reason abs" style="left:203px;top:302px">
    <h4><svg width="30" height="22" viewBox="0 0 30 22" fill="none" stroke="#fff" stroke-width="1.6"><circle cx="15" cy="11" r="8"/><path d="M15 6v5l3 2"/></svg>Efficient and effective 24/7 support</h4>
    <p>Whenever you have a question, our friendly team is ready to help by phone, email or live chat, day or night, so you are never left waiting for the answers you need.</p>
  </div>
  <div class="reason abs" style="left:623px;top:302px">
    <h4><svg width="30" height="22" viewBox="0 0 30 22" fill="none" stroke="#fff" stroke-width="1.6"><rect x="3" y="3" width="24" height="15" rx="1.5"/><path d="M8 21h14M9 13l4-4 3 3 5-5"/></svg>We have the best selection online</h4>
    <p>From term and whole of life cover to critical illness and income protection, you can browse a wide range of policies online and find the right option for every stage of life.</p>
  </div>
</section>

<section class="faq">
  <h2 class="section-title abs">Frequently asked questions</h2>
  <ul class="faq-list abs">
    <li><i class="plus"></i><span>What is life insurance?</span></li>
    <li><i class="plus"></i><span>Who needs life insurance?</span></li>
    <li><i class="plus"></i><span>What's the difference between whole and term life insurance?</span></li>
    <li><i class="plus"></i><span>How are life insurance quotes calculated?</span></li>
    <li><i class="plus"></i><span>Can I get life insurance if I have a medical condition?</span></li>
    <li><i class="plus"></i><span>What information is required when applying for term life insurance?</span></li>
    <li><i class="plus"></i><span>If you are covered under a group life insurance policy through your employer, do you still need a personal policy?</span></li>
  </ul>
</section>

<section class="cta">
  <div class="cta-photo abs" role="img" aria-label="Parent holding a smiling baby at home"></div>
  <h2 class="abs">Compare life insurance quotes - in minutes.</h2>
  <p class="cta-sub abs">Save time and money on life cover</p>
  <a class="btn abs" href="#">Get Started Now</a>
</section>

<footer class="site-footer">
  <div class="brand abs">Kestrova<span class="brand-dot"></span></div>
  <p class="footer-about abs">Kestrova.co.uk (the "Website") is a trading name of Kestrova Digital Ltd. We are registered in England and Wales under company number 11234567 and have our registered office at 14 Marlow Street, London, EC1V 4HP.</p>
  <div class="footer-col abs" style="left:580px;top:32px">
    <h5>Links</h5>
    <ul><li>Home</li><li>About</li><li>Blog</li><li>Contact Us</li></ul>
  </div>
  <div class="footer-col abs" style="left:692px;top:58px">
    <ul><li>Compare Quotes</li><li>FAQ</li><li>Guides</li></ul>
  </div>
  <div class="footer-col abs" style="left:882px;top:32px">
    <h5>Contact Us</h5>
    <ul><li>0300 555 0186</li><li>contact@kestrova.co.uk</li></ul>
    <div class="social" aria-label="Social links"><i></i><i></i></div>
  </div>
  <p class="legal abs">Copyright © 2018 Kestrova<br>Terms and Conditions | Privacy Policy | Cookie Policy</p>
</footer>

</body>
</html>
```